Colin Dwyer Moving DL Flyer

We need a double sided DL flyer to give to patients to let them know that we are moving location.
On one side we would like it to read:
"We Are Moving!" and "November 2017" and our logo.
On the other side we would like it to read:
"Same Great Staff"
"Same Great Service"
"Bigger, Brighter and Better"
"New Location at 52 Fernlow St"
with a map below (attached)
The flyer should follow our practice branding. Attached is a copy of our business card as an example of this.

```html
<!DOCTYPE html>
<html lang="en">
<head>
<meta charset="UTF-8">
<title>Colin Dwyer Optometry – We Are Moving</title>
<link href="https://fonts.googleapis.com/css2?family=Domine:wght@700&family=Roboto:wght@300;400&display=swap" rel="stylesheet">
<style>
  :root {
    --page-bg: #e9e7e4;
    --paper: #ffffff;
    --ink: #1c1c1c;
    --ink-soft: #555555;
    --band-grey: #6e6e6e;
    --rule-grey: #8a8a8a;
    --footer-bg: #222222;
    --footer-text: #ffffff;
  }
  html, body {
    margin: 0;
    padding: 0;
    width: 1200px;
    height: 1200px;
    overflow: hidden;
    background: var(--page-bg);
  }
  .flyer {
    position: absolute;
    left: 378px;
    top: 80px;
    width: 444px;
    height: 1040px;
    background: var(--paper);
    overflow: hidden;
    box-shadow: 0 2px 8px rgba(0,0,0,0.15);
  }
  .headline {
    position: absolute;
    top: 28px;
    left: 0;
    width: 100%;
    margin: 0;
    text-align: center;
    font-family: "Domine", Georgia, serif;
    font-weight: 700;
    font-size: 70px;
    line-height: 68px;
    letter-spacing: -1px;
    color: var(--ink);
  }
  .hero {
    position: absolute;
    top: 216px;
    left: 0;
    width: 444px;
    height: 496px;
  }
  .move-date {
    position: absolute;
    top: 732px;
    left: 0;
    width: 100%;
    margin: 0;
    text-align: center;
    font-family: "Domine", Georgia, serif;
    font-weight: 700;
    font-size: 48px;
    line-height: 48px;
    color: var(--ink);
  }
  .brand {
    position: absolute;
    top: 0;
    left: 0;
    width: 100%;
    height: 100%;
    font-family: "Roboto", Arial, sans-serif;
    color: var(--ink);
  }
  .brand-square {
    position: absolute;
    left: 44px;
    top: 876px;
    width: 60px;
    height: 60px;
    background: var(--ink);
  }
  .brand-rule {
    position: absolute;
    left: 126px;
    top: 852px;
    width: 1px;
    height: 96px;
    background: var(--rule-grey);
  }
  .brand-name {
    position: absolute;
    left: 142px;
    top: 858px;
    font-weight: 300;
    font-size: 28px;
    line-height: 30px;
    letter-spacing: -0.3px;
  }
  .brand-field {
    position: absolute;
    left: 140px;
    top: 884px;
    font-weight: 300;
    font-size: 54px;
    line-height: 60px;
    letter-spacing: -1px;
  }
  .brand-tagline {
    position: absolute;
    left: 142px;
    top: 953px;
    font-weight: 300;
    font-size: 17px;
    line-height: 20px;
    color: var(--ink-soft);
  }
  .site-bar {
    position: absolute;
    bottom: 0;
    left: 0;
    width: 100%;
    height: 44px;
    background: var(--footer-bg);
    color: var(--footer-text);
    font-family: "Roboto", Arial, sans-serif;
    font-weight: 400;
    font-size: 17px;
    letter-spacing: 9.5px;
    line-height: 44px;
    text-align: center;
    text-indent: 9px;
  }
</style>
</head>
<body>
  <main class="flyer">
    <h1 class="headline">We Are<br>Moving!</h1>

    <svg class="hero" viewBox="0 0 444 496" xmlns="http://www.w3.org/2000/svg">
      <defs>
        <linearGradient id="chartTone" x1="0" y1="0" x2="0" y2="1">
          <stop offset="0" stop-color="#f6f8f8"/>
          <stop offset="0.38" stop-color="#e6eaea"/>
          <stop offset="0.5" stop-color="#9aa6a6"/>
          <stop offset="0.62" stop-color="#5d6b6b"/>
          <stop offset="0.78" stop-color="#a7b1b1"/>
          <stop offset="0.92" stop-color="#eef1f1"/>
          <stop offset="1" stop-color="#f4f6f6"/>
        </linearGradient>
      </defs>
      <ellipse class="lens-band" cx="250" cy="248" rx="330" ry="248" fill="var(--band-grey)"/>
      <ellipse class="lens-gap" cx="262" cy="249" rx="322" ry="237" fill="#ffffff"/>
      <ellipse class="lens-photo" cx="268" cy="249" rx="318" ry="231" fill="url(#chartTone)"
               role="img" aria-label="Photo of dark-framed glasses in front of an eye test chart"/>
    </svg>

    <p class="move-date">November<br>2017</p>

    <div class="brand">
      <div class="brand-square"></div>
      <div class="brand-rule"></div>
      <div class="brand-name">Colin Dwyer</div>
      <div class="brand-field">Optometry</div>
      <div class="brand-tagline">See Better. See Us.</div>
    </div>

    <footer class="site-bar">www.colindwyer.com.au</footer>
  </main>
</body>
</html>
```